Need Help having my business card stand out

I am the owner of Pine Ridge Canine Coaching and would like for my business cards to stand out. I have been trying to keep designing them myself but I can't get what I have in my head on the card. I will try my best to post templates that I like for inspirations. I want something unique but elegant. I don't want in to look cartoony or cheesy. It needs to pop in a pet shop but also in a coffee shop or gym.

Target Market(s)

Dog owners, Married ,No young kids Jr High school kids and up (maybe kids on the way) Executives, Stay at home moms/wives, Small business owners

Industry/Entity Type

Dog Training

Contact Information for Business Card

Trevor Holloway, 555-304-7162, info@pineridgecanine.example, www.pineridgecanine.example

Colors

Designer to choose colors to be used in the design.

Requirements
Must have
• my logo
Should not have
• Cursive lettering

```html
<!DOCTYPE html>
<html lang="en">
<head>
<meta charset="utf-8">
<title>Pine Ridge Canine Coaching – Business Card</title>
<link rel="stylesheet" href="https://fonts.googleapis.com/css2?family=Alfa+Slab+One&display=swap">
<style>
  :root {
    --canvas: #efece8;
    --card-red: #c81f26;
    --card-dark: #262627;
    --ink-light: #ffffff;
    --ink-muted: #8d8d8f;
  }
  html, body {
    margin: 0;
    padding: 0;
    width: 1200px;
    height: 960px;
    overflow: hidden;
    background: var(--canvas);
  }
  .card {
    position: absolute;
    left: 250px;
    width: 700px;
    height: 400px;
    overflow: hidden;
    box-shadow: 0 10px 28px rgba(0,0,0,0.18);
  }
  .card-front {
    top: 60px;
    background: var(--card-red);
    display: flex;
    align-items: center;
    justify-content: center;
    color: var(--ink-light);
  }
  .brand-mark {
    display: flex;
    align-items: center;
    gap: 18px;
  }
  .brand-dot {
    width: 22px;
    height: 22px;
    border-radius: 50%;
    background: var(--ink-light);
    flex: none;
  }
  .brand-name {
    font-family: "Alfa Slab One", serif;
    font-size: 38px;
    line-height: 1.15;
    text-align: left;
    color: var(--ink-light);
  }
  .card-back {
    top: 500px;
    background: var(--card-red);
  }
  .back-panel {
    position: absolute;
    inset: 0;
  }
  .holder-name {
    position: absolute;
    left: 52px;
    top: 46px;
    margin: 0;
    font-family: "Alfa Slab One", serif;
    font-weight: 400;
    font-size: 34px;
    line-height: 1.2;
    color: var(--ink-light);
  }
  .contact-list {
    position: absolute;
    left: 52px;
    top: 178px;
    margin: 0;
    padding: 0;
    list-style: none;
    font-family: "Alfa Slab One", serif;
    font-size: 15px;
    color: var(--ink-light);
  }
  .contact-list li {
    display: flex;
    align-items: center;
    gap: 14px;
    margin-bottom: 26px;
  }
  .contact-icon {
    width: 20px;
    height: 20px;
    flex: none;
  }
  .panel-brand {
    position: absolute;
    right: 36px;
    top: 160px;
    width: 230px;
    font-family: "Alfa Slab One", serif;
    font-size: 28px;
    line-height: 1.15;
    text-align: center;
    color: var(--ink-muted);
  }
</style>
</head>
<body>
  <section class="card card-front" aria-label="Business card front">
    <div class="brand-mark">
      <span class="brand-dot"></span>
      <span class="brand-name">Pine Ridge<br>Canine Coaching</span>
    </div>
  </section>

  <section class="card card-back" aria-label="Business card back">
    <svg class="back-panel" width="700" height="400" viewBox="0 0 700 400" aria-hidden="true">
      <polygon points="460,52 700,52 700,400 380,400" fill="var(--card-dark)"/>
    </svg>
    <h1 class="holder-name">Trevor Holloway</h1>
    <ul class="contact-list">
      <li>
        <svg class="contact-icon" viewBox="0 0 20 20" aria-hidden="true"><path d="M4 2l4 1 1 4-2 2c1 2 3 4 5 5l2-2 4 1 1 4-2 2C9 19 1 11 2 4z" fill="#fff"/></svg>
        555-304-7162
      </li>
      <li>
        <svg class="contact-icon" viewBox="0 0 20 20" aria-hidden="true"><rect x="1.5" y="4.5" width="17" height="11" fill="none" stroke="#fff" stroke-width="1.6"/><path d="M1.5 4.5l8.5 6.5 8.5-6.5" fill="none" stroke="#fff" stroke-width="1.6"/></svg>
        info@pineridgecanine.example
      </li>
      <li>
        <svg class="contact-icon" viewBox="0 0 20 20" aria-hidden="true"><circle cx="10" cy="10" r="8" fill="none" stroke="#fff" stroke-width="1.6"/><ellipse cx="10" cy="10" rx="3.5" ry="8" fill="none" stroke="#fff" stroke-width="1.4"/><path d="M2 10h16" stroke="#fff" stroke-width="1.4"/></svg>
        www.pineridgecanine.example
      </li>
    </ul>
    <div class="panel-brand">Pine Ridge Canine Coaching</div>
  </section>
</body>
</html>
```